I have an account on Plumetry through Tanvrik, so the design will need to be built there. I already have a logo, and the design of the website should at least compliment the look of the logo. The placeholder website where the logo can be seen is at www.velmarconsulting.example. The purpose of the website at this point in time is not to drive business, but rather, to have a strong appearance and add some credibility to my already existing business.

The website should have some level of abstraction about it. I prefefer designs and shapes of images of people. The fewer people, the better. No stock photography of people standing around talking to each other.

Number of Pages Required

4 page

Requirements
Must have
• The ability to work on my existing Plume Try Account
Should not have
• Stock photography of people standing around doing "business-y" stuff. That is sooo old and played out, and is the opposite of the type of message I am trying to portray.

```html
<!DOCTYPE html>
<html lang="en">
<head>
<meta charset="utf-8">
<title>Velmar Consulting</title>
<link href="https://fonts.googleapis.com/css2?family=Open+Sans:wght@400;600;700&family=Roboto:wght@300;400;700;900&display=swap" rel="stylesheet">
<style>
:root{
  --orange:#f27420;
  --orange-deep:#e2611a;
  --dark:#121212;
  --ink:#111;
  --muted:#6b6b6b;
  --light:#f0f0f0;
  --field:#dcdcdc;
  --white:#fff;
  --art-light:#eceef3;
  --art-mid:#d3d6df;
}
*{box-sizing:border-box;margin:0;padding:0}
html,body{width:1200px;height:3814px;overflow:hidden;background:var(--white)}
body{position:relative;font-family:"Open Sans",sans-serif;color:var(--ink)}
.abs{position:absolute}
.heading{font-family:"Roboto",sans-serif;font-weight:700;font-size:50px;letter-spacing:.5px;text-align:center;width:1200px;left:0}
.heading .accent{color:var(--orange)}
.body-copy{font-size:12.5px;line-height:19px;color:var(--muted)}

/* hero */
.hero{top:0;left:0;width:1200px;height:760px;overflow:hidden}
.hero-bg{left:0;top:0;width:1200px;height:674px;background:linear-gradient(180deg,#0c0c0d 0%,#1a1a1c 100%)}
.hero-art{left:0;top:0}
.brand{left:170px;top:16px;display:flex;align-items:center;gap:10px;color:var(--white);font-weight:700;font-size:22px}
.brand .mark{width:26px;height:26px;background:var(--white)}
.nav{left:416px;top:36px;display:flex;gap:6px;font-size:13px;font-weight:600;color:var(--white)}
.nav a{color:inherit;text-decoration:none;padding:5px 13px}
.nav a.active{background:var(--orange)}
.top-phone{left:905px;top:38px;display:flex;align-items:center;gap:10px;color:var(--white);font-size:12px;font-weight:600}
.hero-title{left:163px;top:170px;font-family:"Roboto",sans-serif;font-weight:700;font-size:76px;letter-spacing:2px;color:var(--orange)}
.hero-sub{left:163px;top:252px;font-size:28px;color:var(--white)}
.hero-sub b{font-weight:700}
.hero-text{left:163px;top:296px;width:420px;font-size:15px;line-height:21px;color:#e6e6e6}
.btn-light{left:163px;top:372px;width:185px;height:48px;background:var(--white);color:var(--ink);font-weight:700;font-size:15px;display:flex;align-items:center;justify-content:center;letter-spacing:.5px}
.slide-btn{top:526px;width:44px;height:44px;border:2px solid #bbb;display:flex;align-items:center;justify-content:center}

/* services */
.service{display:flex;gap:30px;width:380px}
.service .icon{width:104px;height:104px;flex:none;border-radius:48% 52% 44% 56%;background:linear-gradient(135deg,#f6e9e1,#e8e3e0);display:flex;align-items:center;justify-content:center}
.service h3{font-size:14px;font-weight:700;margin:6px 0 8px}
.service p{font-size:11.5px;line-height:18px;color:var(--muted);width:240px}

/* about */
.btn-dark{background:var(--ink);color:var(--white);font-size:12px;font-weight:600;display:flex;align-items:center;justify-content:center}
.about-art{left:615px;top:1310px;width:405px;height:370px}

/* clients */
.clients{top:1774px;left:0;width:1200px;height:323px;background:linear-gradient(90deg,#121213,#232325 70%,#151516)}
.client-photo{left:160px;top:1861px;width:265px;height:320px;background:linear-gradient(180deg,#6f6257 0%,#a8927e 45%,#7b8a6c 80%,#4a4038 100%)}

/* news */
.card{top:2351px;width:280px;height:377px;background:var(--white);box-shadow:0 1px 8px rgba(0,0,0,.18)}
.card .thumb{height:186px}
.card .date{margin:16px 0 0 16px;font-size:10px;color:var(--orange);display:flex;gap:6px;align-items:center}
.card h4{margin:12px 16px 0;font-size:13px;font-weight:700;white-space:nowrap}
.card p{margin:10px 16px 0;font-size:11.5px;line-height:18px;color:var(--muted)}
.card .more{margin:18px 0 0 16px;width:86px;height:28px;font-size:10.5px;font-weight:700}

/* contact */
.contact-bg{top:2827px;left:0;width:1200px;height:493px;background:var(--light)}
.contact-photo{top:2827px;left:0;width:635px;height:493px;background:linear-gradient(90deg,#e4e6e8 0%,#b9b2a9 22%,#6b5f56 45%,#3d3a3b 70%,#8b8884 88%,#f0f0f0 100%)}
.field{background:var(--field);font-size:10px;color:#444;padding:7px 8px}
.btn-orange{background:var(--orange);color:var(--white);font-weight:700;font-size:12px;display:flex;align-items:center;justify-content:center}

/* newsletter */
.newsletter{top:3320px;left:0;width:1200px;height:117px;background:var(--orange)}

/* footer */
.footer{top:3437px;left:0;width:1200px;height:377px;background:linear-gradient(90deg,#151517,#242427 60%,#18181a)}
.foot-title{font-size:12px;font-weight:700;color:var(--orange);letter-spacing:.5px}
.foot-list{list-style:none;font-size:11.5px;color:#ddd}
.foot-list li{display:flex;align-items:center;gap:14px;height:33px}
.bullet{width:5px;height:5px;background:var(--orange);border-radius:50%}
.social-dot{width:24px;height:24px;border-radius:50%;background:var(--white)}
.copyright{top:3780px;left:0;width:1200px;text-align:center;font-size:11px;color:#ddd}
</style>
</head>
<body>

<!-- Hero -->
<header class="hero abs">
  <div class="hero-bg abs"></div>
  <svg class="hero-wave abs" style="left:0;top:0" width="1200" height="760" viewBox="0 0 1200 760">
    <path d="M0 540 C120 620 210 660 330 610 C450 560 560 530 700 560 C820 585 960 600 1200 560 L1200 760 L0 760 Z" fill="var(--orange)"/>
    <path d="M0 590 C130 660 230 690 350 650 C470 610 580 585 720 605 C850 625 980 640 1200 610 L1200 760 L0 760 Z" fill="var(--white)"/>
  </svg>
  <svg class="hero-art abs" width="1200" height="760" viewBox="0 0 1200 760" role="img" aria-label="Isometric illustration of a production line with screens, charts and a small worker">
    <defs>
      <linearGradient id="artFill" x1="0" y1="0" x2="1" y2="1">
        <stop offset="0" stop-color="#f7f7fa"/>
        <stop offset="1" stop-color="#cfd2db"/>
      </linearGradient>
    </defs>
    <path d="M560 520 L760 410 L760 330 L900 250 L1200 250 L1200 700 L1080 760 L780 760 L560 640 Z" fill="url(#artFill)"/>
  </svg>
  <div class="brand abs"><span class="mark"></span>Velmar</div>
  <nav class="nav abs">
    <a class="active">Home</a><a>About us</a><a>Services</a><a>Clients</a><a>Contact</a>
  </nav>
  <div class="top-phone abs">
    <svg width="14" height="14" viewBox="0 0 24 24"><path d="M6.6 10.8a15 15 0 0 0 6.6 6.6l2.2-2.2c.3-.3.7-.4 1-.2 1.1.4 2.3.6 3.6.6.6 0 1 .4 1 1V20c0 .6-.4 1-1 1A17 17 0 0 1 3 4c0-.6.4-1 1-1h3.5c.6 0 1 .4 1 1 0 1.3.2 2.5.6 3.6.1.3 0 .7-.2 1z" fill="var(--orange)"/></svg>
    +01-2345-678-900
  </div>
  <h1 class="hero-title abs">VELMAR</h1>
  <p class="hero-sub abs">A Specialized <b>Brand</b> Consultancy.</p>
  <p class="hero-text abs">We help our clients identify and develop protectable source identifiers through asset creation-oriented strategies.</p>
  <div class="btn-light abs">CONTACT US</div>
  <div class="slide-btn abs" style="left:163px"><svg width="12" height="14" viewBox="0 0 12 14"><path d="M9 1 3 7l6 6" stroke="#fff" stroke-width="2" fill="none"/></svg></div>
  <div class="slide-btn abs" style="left:221px"><svg width="12" height="14" viewBox="0 0 12 14"><path d="M3 1l6 6-6 6" stroke="#fff" stroke-width="2" fill="none"/></svg></div>
</header>

<!-- Services -->
<h2 class="heading abs" style="top:795px"><span class="accent">OUR</span> SERVICES</h2>
<div class="service abs" style="left:178px;top:902px">
  <div class="icon"><svg width="50" height="50" viewBox="0 0 50 50" fill="none" stroke="var(--orange)" stroke-width="2.5"><circle cx="21" cy="21" r="12"/><path d="M30 30l12 12"/></svg></div>
  <div><h3>Brand Research</h3><p>Lorem Ipsum is simply dummy text of the printing and typesetting industry. Lorem Ipsum has been the industry's standard dummy text ever since the 1500s</p></div>
</div>
<div class="service abs" style="left:623px;top:902px">
  <div class="icon"><svg width="50" height="50" viewBox="0 0 50 50" fill="none" stroke="var(--orange)" stroke-width="2.5"><circle cx="25" cy="25" r="16"/><circle cx="25" cy="25" r="7"/><path d="M25 4v6M25 40v6M4 25h6M40 25h6"/></svg></div>
  <div><h3>Brand Strategy</h3><p>Lorem Ipsum is simply dummy text of the printing and typesetting industry. Lorem Ipsum has been the industry's standard dummy text ever since the 1500s</p></div>
</div>
<div class="service abs" style="left:178px;top:1074px">
  <div class="icon"><svg width="50" height="50" viewBox="0 0 50 50" fill="none" stroke="var(--orange)" stroke-width="2.5"><circle cx="25" cy="21" r="12"/><path d="M19 37h12M21 43h8"/></svg></div>
  <div><h3>Creative and Design</h3><p>Lorem Ipsum is simply dummy text of the printing and typesetting industry. Lorem Ipsum has been the industry's standard dummy text ever since the 1500s</p></div>
</div>
<div class="service abs" style="left:623px;top:1074px">
  <div class="icon"><svg width="50" height="50" viewBox="0 0 50 50" fill="none" stroke="var(--orange)" stroke-width="2.5"><circle cx="25" cy="14" r="6"/><circle cx="11" cy="36" r="6"/><circle cx="39" cy="36" r="6"/><path d="M22 19l-8 12M28 19l8 12M17 36h16"/></svg></div>
  <div><h3>Management</h3><p>Lorem Ipsum is simply dummy text of the printing and typesetting industry. Lorem Ipsum has been the industry's standard dummy text ever since the 1500s</p></div>
</div>

<!-- About -->
<h2 class="heading abs" style="top:1295px;left:163px;width:auto;text-align:left"><span class="accent">ABOUT</span> US</h2>
<div class="body-copy abs" style="left:163px;top:1418px;width:420px">
  <p>Lorem Ipsum is simply dummy text of the printing and typesetting industry. Lorem Ipsum has been the industry's standard dummy text ever since the 1500s, when an unknown printer took a galley of type and scrambled it to make a type specimen book.</p>
  <p style="margin-top:10px">It has survived not only five centuries, but also the leap into electronic typesetting, remaining essentially unchanged.</p>
  <p style="margin-top:10px">It was popularised in the 1960s with the release of Transfix sheets containing Lorem Ipsum passages, and more recently with desktop publishing software like Folio Layout including versions of Lorem Ipsum.</p>
</div>
<div class="btn-dark abs" style="left:163px;top:1640px;width:186px;height:43px">LET'S STARTED NOW</div>
<svg class="about-art abs" width="405" height="370" viewBox="0 0 405 370" role="img" aria-label="Flat illustration of a team reviewing charts on a large dashboard">
  <defs>
    <linearGradient id="aboutFill" x1="0" y1="0" x2="0" y2="1">
      <stop offset="0" stop-color="#f3f4f9"/>
      <stop offset="1" stop-color="#dfe2ec"/>
    </linearGradient>
  </defs>
  <path d="M90 20 L330 60 L330 250 L405 290 L405 350 L60 370 L0 330 L0 200 L90 170 Z" fill="url(#aboutFill)"/>
</svg>

<!-- Clients -->
<section class="clients abs"></section>
<div class="client-photo abs" role="img" aria-label="Photo of three smiling clients"></div>
<h2 class="abs" style="left:521px;top:1855px;font-family:'Roboto',sans-serif;font-weight:700;font-size:43px;color:var(--white)">Some from out clients</h2>
<svg class="abs" style="left:521px;top:1922px" width="18" height="16" viewBox="0 0 18 16"><path d="M0 16V8C0 3 3 0 7 0v3C5 3 4 5 4 7h3v9zM11 16V8c0-5 3-8 7-8v3c-2 0-3 2-3 4h3v9z" fill="#fff"/></svg>
<p class="abs" style="left:563px;top:1918px;width:430px;font-size:11.5px;line-height:17px;color:#eee">Lorem Ipsum is simply dummy text of the printing and typesetting industry. Lorem Ipsum has been the industry's standard dummy text ever since the 1500s, when an unknown printer took a galley of type and scrambled it to make a type specimen book.</p>
<p class="abs" style="left:563px;top:1996px;font-size:13px;font-weight:600;color:var(--orange)">-Client Name</p>
<p class="abs" style="left:563px;top:2018px;font-size:11.5px;color:#ccc">Lorem Ipsum is</p>
<svg class="abs" style="left:472px;top:2114px" width="40" height="16" viewBox="0 0 40 16"><path d="M8 2 2 8l6 6M32 2l6 6-6 6" stroke="var(--orange)" stroke-width="2" fill="none"/></svg>

<!-- News -->
<h2 class="heading abs" style="top:2248px"><span class="accent">OUR</span> NEWS</h2>
<article class="card abs" style="left:160px">
  <div class="thumb" role="img" aria-label="Photo of hands reviewing printed charts" style="background:linear-gradient(135deg,#e3e7ed,#a9b8ca 60%,#eef0f2)"></div>
  <div class="date"><svg width="10" height="10" viewBox="0 0 10 10"><rect x="1" y="2" width="8" height="7" fill="none" stroke="var(--orange)"/></svg>15 January 2019</div>
  <h4>Lorem Ispsum is simply dummy text.</h4>
  <p>Lorem Ipsum is simply dummy text of the printing and typesetting industry.</p>
  <div class="more btn-dark">READ MORE</div>
</article>
<article class="card abs" style="left:460px">
  <div class="thumb" role="img" aria-label="Top-down photo of a desk with a laptop and notes" style="background:linear-gradient(135deg,#c8702f,#b0592a 55%,#7a5443)"></div>
  <div class="date"><svg width="10" height="10" viewBox="0 0 10 10"><rect x="1" y="2" width="8" height="7" fill="none" stroke="var(--orange)"/></svg>15 January 2019</div>
  <h4>Lorem Ispsum is simply dummy text.</h4>
  <p>Lorem Ipsum is simply dummy text of the printing and typesetting industry.</p>
  <div class="more btn-dark">READ MORE</div>
</article>
<article class="card abs" style="left:760px">
  <div class="thumb" role="img" aria-label="Photo of a small team working at a laptop" style="background:linear-gradient(135deg,#2d2f35,#5c5f66 55%,#24262b)"></div>
  <div class="date"><svg width="10" height="10" viewBox="0 0 10 10"><rect x="1" y="2" width="8" height="7" fill="none" stroke="var(--orange)"/></svg>15 January 2019</div>
  <h4>Lorem Ispsum is simply dummy text.</h4>
  <p>Lorem Ipsum is simply dummy text of the printing and typesetting industry.</p>
  <div class="more btn-dark">READ MORE</div>
</article>

<!-- Contact -->
<section class="contact-bg abs"></section>
<div class="contact-photo abs" role="img" aria-label="Photo of two colleagues looking at a laptop and tablet"></div>
<h2 class="abs" style="left:637px;top:2885px;font-family:'Roboto',sans-serif;font-weight:700;font-size:50px"><span style="color:var(--orange)">CONTACT</span> US</h2>
<p class="abs" style="left:640px;top:2942px;font-size:12px;font-weight:600">Lorem Ipsum is simply dummy text of the printing and typesetting.</p>
<div class="field abs" style="left:640px;top:3002px;width:186px;height:36px">Name:</div>
<div class="field abs" style="left:836px;top:3002px;width:186px;height:36px">Phone</div>
<div class="field abs" style="left:640px;top:3048px;width:382px;height:33px">Email:</div>
<div class="field abs" style="left:640px;top:3091px;width:382px;height:109px">Message:</div>
<div class="btn-orange abs" style="left:640px;top:3223px;width:90px;height:36px">SUBMIT</div>

<!-- Newsletter -->
<section class="newsletter abs"></section>
<p class="abs" style="left:165px;top:3349px;font-family:'Roboto',sans-serif;font-weight:300;font-size:50px;color:var(--white);line-height:58px">Newsletter</p>
<div class="abs" style="left:516px;top:3358px;width:313px;height:38px;background:var(--white);font-size:11px;padding:11px 8px">Eamil</div>
<div class="btn-dark abs" style="left:829px;top:3358px;width:81px;height:38px;font-weight:700">SUBMIT</div>

<!-- Footer -->
<footer class="footer abs"></footer>
<div class="abs" style="left:224px;top:3503px;display:flex;align-items:center;gap:10px;color:var(--white);font-weight:700;font-size:20px"><span style="width:26px;height:26px;background:var(--white)"></span>Velmar</div>
<p class="abs" style="left:163px;top:3602px;width:200px;font-size:11px;line-height:17px;color:#ddd">Lorem Ipsum is simply dummy text of the printing and typesetting industry. Lorem Ipsum has been the industry's standard dummy text ever since the 1500s.</p>

<p class="foot-title abs" style="left:386px;top:3495px">SITEMAP</p>
<ul class="foot-list abs" style="left:400px;top:3540px">
  <li><span class="bullet"></span>Home</li>
  <li><span class="bullet"></span>About us</li>
  <li><span class="bullet"></span>Services</li>
  <li><span class="bullet"></span>Clients</li>
  <li><span class="bullet"></span>Contact us</li>
</ul>

<p class="foot-title abs" style="left:613px;top:3495px">OUR INFO</p>
<ul class="foot-list abs" style="left:613px;top:3548px;font-size:10px">
  <li style="height:56px"><svg width="24" height="24" viewBox="0 0 24 24"><circle cx="12" cy="12" r="11" fill="none" stroke="#fff" stroke-width="1.5"/><path d="M9 7l2 3-1.5 1.5a8 8 0 0 0 3 3L14 13l3 2-1.5 2C11 17 7 13 7 8.5z" fill="#fff"/></svg>+01-2345-678-900</li>
  <li style="height:64px;align-items:flex-start"><svg width="24" height="24" viewBox="0 0 24 24"><circle cx="12" cy="12" r="11" fill="none" stroke="#fff" stroke-width="1.5"/><path d="M12 5a4 4 0 0 0-4 4c0 3 4 9 4 9s4-6 4-9a4 4 0 0 0-4-4z" fill="#fff"/></svg><span style="width:110px;line-height:13px">215 600 Lorem Ipsum Simply dummy text.</span></li>
  <li style="height:40px"><svg width="24" height="24" viewBox="0 0 24 24"><circle cx="12" cy="12" r="11" fill="none" stroke="#fff" stroke-width="1.5"/><rect x="6.5" y="8" width="11" height="8" fill="none" stroke="#fff" stroke-width="1.3"/><path d="M6.5 8l5.5 4.5L17.5 8" fill="none" stroke="#fff" stroke-width="1.3"/></svg>info@velmarconsulting.example</li>
</ul>

<p class="foot-title abs" style="left:841px;top:3495px">GET IN TOUCH</p>
<ul class="foot-list abs" style="left:841px;top:3545px">
  <li style="height:38px"><span class="social-dot"></span>Pagebook</li>
  <li style="height:38px"><span class="social-dot"></span>Linkwork</li>
  <li style="height:38px"><span class="social-dot"></span>Chirper</li>
  <li style="height:38px"><span class="social-dot"></span>Circleplus</li>
</ul>

<p class="copyright abs">©2019 <b>Velmar Consulting</b>. All Right Reserved. | Terms &amp; Conditions.</p>

</body>
</html>
```